Website for Party

Design a new website for PlumtreeGatherings.net
We have attached the new logos and please look at the website, and our facebook page: facebook.com/plumtreegatherings for inspiration
Updates

Hi Guys, please be original with all designs and images otherwise the design will be eliminated Thank you

some of your designs have too much happening in them, others make it clear that the designer has not yet read the brief fully

Please everyone be original!

```html
<!DOCTYPE html>
<html lang="en">
<head>
<meta charset="utf-8">
<title>Plumtree Gatherings – Harbor Cruise Party</title>
<link rel="stylesheet" href="https://fonts.googleapis.com/css2?family=Open+Sans:wght@300;400;700&family=Roboto+Condensed:wght@400;700&display=swap">
<style>
:root{
  --ink:#050507;
  --nav:#7a7a7c;
  --red:#d8213f;
  --red-deep:#8d0f22;
  --white:#ffffff;
  --muted:#d8d8d8;
  --social:#3d6fb6;
}
*{margin:0;padding:0;box-sizing:border-box}
html,body{width:792px;height:1200px;overflow:hidden;background:var(--ink)}
body{position:relative;font-family:"Open Sans",Arial,sans-serif;color:var(--white)}
.backdrop{position:absolute;inset:0;background:
  radial-gradient(circle at 40px 700px,rgba(160,40,90,.45),transparent 130px),
  radial-gradient(circle at 760px 760px,rgba(200,160,60,.35),transparent 120px),
  radial-gradient(circle at 760px 1020px,rgba(120,180,90,.3),transparent 120px),
  linear-gradient(#070709 0,#0a0a10 60%,#140d18 100%)}
.header{position:absolute;left:0;top:0;width:792px;height:68px;background:linear-gradient(#0b0b0e,#1a1a22)}
.brand{position:absolute;left:90px;top:16px;display:flex;align-items:center;gap:8px;font-size:23px;letter-spacing:5px}
.brand .mark{width:36px;height:36px;border-radius:50%;background:var(--white)}
.social{position:absolute;display:flex;gap:6px}
.social span{width:18px;height:18px;border-radius:2px;background:var(--social)}
.social span:nth-child(3){background:#8a7a66}
.social span:nth-child(4){background:#bfbfbf}
.social span:nth-child(6){background:#c92a2a}
.header .social{left:566px;top:24px}
.nav{position:absolute;left:0;top:68px;width:792px;height:40px;background:var(--nav)}
.nav ul{list-style:none;position:absolute;left:87px;top:0;display:flex;height:40px;font-family:"Roboto Condensed",Arial,sans-serif;font-size:11.5px;font-weight:700}
.nav li{display:flex;align-items:center;padding:0 14px}
.nav li.active{background:var(--red);width:80px;justify-content:center;margin-right:9px}
.phone{position:absolute;right:78px;top:8px;font-size:18px;font-weight:300;white-space:nowrap}
.phone b{font-weight:700}
.hero{position:absolute;left:0;top:108px;width:792px;height:325px;background:
  radial-gradient(ellipse at 400px 60px,rgba(255,240,250,.55),transparent 200px),
  radial-gradient(ellipse at 560px 230px,rgba(180,170,190,.35),transparent 160px),
  linear-gradient(#3c2a3a,#5a3a4e 45%,#1c1418)}
.arrow{position:absolute;top:115px;width:37px;height:37px;background:var(--red);display:flex;align-items:center;justify-content:center}
.arrow.prev{left:0}.arrow.next{right:0}
.mailing{position:absolute;left:87px;top:433px;width:618px;height:49px;background:linear-gradient(var(--red),#b81733);display:flex;align-items:center;padding-left:15px;font-size:9.3px;white-space:nowrap}
.mailing .field{margin-left:9px;width:224px;height:22px;background:var(--white);color:#999;font-size:7px;display:flex;align-items:center;padding-left:6px}
.mailing .submit{margin-left:6px;width:82px;height:22px;background:var(--red-deep);font-family:"Roboto Condensed",Arial,sans-serif;font-weight:700;font-size:11px;display:flex;align-items:center;justify-content:center}
.tile{position:absolute;overflow:hidden}
.tile .photo{position:absolute;inset:0}
.tile .copy{position:absolute}
.tile h2{font-size:20px;font-weight:300;line-height:24px;white-space:nowrap}
.tile h2 b{font-weight:700}
.tile p{font-size:8.2px;line-height:10.4px;margin-top:4px;color:var(--muted)}
.tile p u{color:var(--white)}
.col-l{left:87px;width:309px}
.col-r{left:408px;width:297px}
.row1{top:495px;height:148px}
.row2{top:656px;height:148px}
.row3{top:817px;height:148px}
.row4{top:977px;height:149px}
.footer-social{left:87px;top:1141px}
.footer-nav{position:absolute;left:87px;top:1164px;display:flex;gap:12px;font-family:"Roboto Condensed",Arial,sans-serif;font-weight:700;font-size:11px}
.copyright{position:absolute;left:87px;top:1180px;font-size:7.5px;color:var(--muted)}
.footer-brand{position:absolute;left:490px;top:1145px;display:flex;align-items:center;gap:8px;font-size:24px;letter-spacing:5px;color:#9a9a9e}
.footer-brand .mark{width:40px;height:40px;border-radius:50%;background:#9a9a9e}
</style>
</head>
<body>
<div class="backdrop" role="img" aria-label="Night harbor skyline with fireworks"></div>

<header class="header">
  <div class="brand"><span class="mark"></span>Plumtree</div>
  <div class="social"><span></span><span></span><span></span><span></span><span></span><span></span></div>
</header>

<nav class="nav">
  <ul>
    <li class="active">WELCOME</li><li>ABOUT</li><li>FAQ</li><li>ORDER TICKETS</li><li>CONTACT US</li>
  </ul>
  <div class="phone">Phone: <b>555 018 4427</b></div>
</nav>

<section class="hero" role="img" aria-label="DJ performing to a huge festival crowd under stage lights">
  <div class="arrow prev"><svg width="16" height="20" viewBox="0 0 16 20"><path d="M14 2 3 10l11 8" fill="none" stroke="#fff" stroke-width="2"/></svg></div>
  <div class="arrow next"><svg width="16" height="20" viewBox="0 0 16 20"><path d="M2 2l11 8-11 8" fill="none" stroke="#fff" stroke-width="2"/></svg></div>
</section>

<form class="mailing">
  Enter your email address below to be added to our mailing list:
  <div class="field">Add Email Address Here</div>
  <div class="submit">SUBMIT</div>
</form>

<article class="tile col-l row1">
  <div class="photo" role="img" aria-label="Yacht cruising past the Manhattan skyline at night" style="background:linear-gradient(90deg,#2a2f3c 0,#343a48 81%,#2e3fa0 81%,#1a2a70)"></div>
  <div class="copy" style="left:10px;top:30px;width:190px">
    <h2>3+ Hour Cruise<br>around <b>NYC Harbor</b></h2>
    <p style="width:180px">Over 3 hours of cruising through the NYC harbor. Enjoy the open-air deck and admire magnificent views of Manhattan's stunning skyline at sunset with your sweetheart</p>
  </div>
</article>

<article class="tile col-r row1">
  <div class="photo" role="img" aria-label="Singer performing on an outdoor stage" style="background:linear-gradient(#8a8a86 0,#bdb7ac 39%,#d24a6a 40%,#c23356)"></div>
  <div class="copy" style="left:10px;top:66px;width:280px">
    <h2>Opening Performance by<br><b>Tomas Reinholt</b></h2>
    <p style="color:#fff">Up and Coming Musical sensation <u>Tomas Reinholt</u> will perform the National Anthem to kick off the cruise and he will lead an acoustic session on the outdoor deck of the yacht.</p>
  </div>
</article>

<article class="tile col-l row2">
  <div class="photo" role="img" aria-label="Glass of white wine at a bar" style="background:linear-gradient(90deg,#7a5f2e 0,#a78a4c 81%,#cfc6b0 81%,#9a9280)"></div>
  <div class="copy" style="left:10px;top:16px;width:195px">
    <h2>Open Premium<br><b>Bar</b></h2>
    <p style="width:190px;margin-top:8px">Enjoy your choice of beer, whiskey, tequila, vodka, and wine, or have one of our professional bartenders prepare your favorite mixed drink. Attend our private lounge with a delicious cocktail and watch the stunning view of Manhattan's skyline.</p>
  </div>
</article>

<article class="tile col-r row2">
  <div class="photo" role="img" aria-label="Plated hors d'oeuvres with fresh greens" style="background:linear-gradient(90deg,#5a5530 0,#6d6a3a 78%,#d8c24a 78%,#8a9a40)"></div>
  <div class="copy" style="left:12px;top:38px;width:185px">
    <h2><b>Hors d’oeuvres</b></h2>
    <p>Enjoy light refreshments while waiting to board the yacht. Hand-baked by refreshments created by our executive chef and served by our own private waiters.</p>
  </div>
</article>

<article class="tile col-l row3">
  <div class="photo" role="img" aria-label="Couple arriving on a red carpet" style="background:linear-gradient(90deg,#a82a2a 0,#7a1e24 39%,#8d2226 39%,#6a1a20)"></div>
  <div class="copy" style="left:111px;top:18px;width:192px">
    <h2>Red Carpet <b>Entry</b></h2>
    <p>Arrive on the pier and walk down the red carpet with your group. A team of professional photographers will capture your red carpet grand entrance. All of the red carpet photos will be touched up by professional graphic artists and made available on the website and on <u>Plumtree's photo gallery</u> after the event.</p>
  </div>
</article>

<article class="tile col-r row3">
  <div class="photo" role="img" aria-label="DJ mixing under blue club lights" style="background:linear-gradient(90deg,#2a5ad8 0,#3a3ab0 36%,#1c1e6a 36%,#1a1c50)"></div>
  <div class="copy" style="left:99px;top:30px;width:192px">
    <h2>Epic Mixes by<br><b>DJ Corvell</b></h2>
    <p>Hit the floor and enjoy hiphop DJ Corvell's spin sessions. With millions of light combinations on the dance floor, <u>DJ Corvell</u> will entertain with freestyle sessions.</p>
  </div>
</article>

<article class="tile col-l row4">
  <div class="photo" role="img" aria-label="Gift bag with red tissue paper" style="background:linear-gradient(90deg,#c9a88a 0,#d86040 39%,#e0452e 39%,#c8361f)"></div>
  <div class="copy" style="left:111px;top:30px;width:190px">
    <h2>Personalized<br><b>Gift Bag</b></h2>
    <p style="color:#fff">As you disembark you will receive your custom gift bag to take home with you which will include souvenirs.</p>
  </div>
</article>

<article class="tile col-r row4">
  <div class="photo" role="img" aria-label="Gourmet buffet dishes" style="background:linear-gradient(90deg,#b06a30 0,#8a4a22 36%,#c25a1a 36%,#a8420f)"></div>
  <div class="copy" style="left:99px;top:44px;width:185px">
    <h2>Premium <b>Buffet</b></h2>
    <p style="color:#fff">Savor the taste of an exquisite delicacies created by our executive chef exclusively for this event.</p>
  </div>
</article>

<footer>
  <div class="social footer-social"><span></span><span></span><span></span><span></span><span></span><span></span></div>
  <div class="footer-nav"><span>WELCOME</span><span>ABOUT</span><span>FAQ</span><span>ORDER TICKETS</span><span>CONTACT US</span></div>
  <div class="copyright">Copyright Plumtree Gatherings.</div>
  <div class="footer-brand"><span class="mark"></span>Plumtree</div>
</footer>
</body>
</html>
```